Web Design for Meadowfield Turf Crew

Meadowfield Turf Crew needs the photoshop files for a simple, clean and professional web design. I need a home and subpage design, although they can be very similar. See pagestridehub.com for a desired layout, although I'd like to see more design than shown on that site. The goal of the site is to attract both lawn maintenance/landscape customers and build a partner network of consultants that serve the US market. The following are needed:

- home and subpage design
- page: Home, Services, Locations, Consultants, FAQ, Contact
- if subpages have header photo, need to include 5 different header photos for each page
- favicon
Updates

I'll award the design based on the homepage concept. The minor subpage changes and other elements can be worked out in the workroom stage. Thanks, Trent

Industry/Entity Type

It Professional

```html
<!DOCTYPE html>
<html lang="en">
<head>
<meta charset="utf-8">
<title>Meadowfield Turf Crew — About &amp; Contact</title>
<link rel="stylesheet" href="https://fonts.googleapis.com/css2?family=Jost:wght@400;500;600&family=Questrial&family=Open+Sans:wght@400;700&display=swap">
<style>
:root{
  --green:#6db33f;
  --green-dark:#4f9a23;
  --ink:#333335;
  --body:#2b2b2b;
  --light-bg:#f2f2f2;
  --field-border:#c9c9c9;
  --placeholder:#9a9a9a;
  --footer:#5f6062;
  --footer-link:#c3c4c6;
  --base:#363636;
  --link-blue:#2fa4e7;
  --button-grey:#7f7f7f;
}
*{box-sizing:border-box;margin:0;padding:0}
html,body{width:1200px;height:1000px;overflow:hidden}
body{position:relative;background:#fff;font-family:"Questrial",sans-serif;color:var(--body)}
.abs{position:absolute}

.intro{left:0;top:0;width:1200px;height:453px;background:var(--light-bg)}
.section-title{font-family:"Jost",sans-serif;font-weight:600;font-size:28px;color:var(--ink);letter-spacing:-.2px;line-height:1}
.section-title .accent{color:var(--green)}
.signup-title .accent{color:var(--green-dark)}
.about-title{left:134px;top:38px}
.about-copy{left:131px;top:102px;width:370px;font-size:13.3px;line-height:16.1px}
.about-copy p+p{margin-top:16px}

.signup{left:525px;top:20px;width:535px;height:412px;
  background:linear-gradient(180deg,#c6e1ef 0%,#dde9ee 30%,#9cb98a 52%,#5f8f35 68%,#7aa64a 82%,#a9bfae 100%)}
.signup-panel{left:76px;top:0;width:388px;height:412px;border-radius:0 0 8px 8px;background:rgba(236,241,242,.72)}
.signup-title{left:110px;top:19px}
.field{position:absolute;left:110px;width:323px;height:25px;background:#fff;border:1px solid var(--field-border);
  font-family:"Jost",sans-serif;font-size:13px;color:var(--placeholder);padding:3px 7px}
.field.message{height:151px}
.submit{left:307px;top:364px;width:126px;height:37px;background:var(--green);color:#fff;
  font-family:"Jost",sans-serif;font-size:16px;display:flex;align-items:center;justify-content:center;letter-spacing:.3px}

.locator{left:131px;top:476px;width:760px;height:187px;border:1.5px solid var(--green);border-radius:8px;overflow:hidden;
  background:linear-gradient(90deg,#f1e4cf 0%,#e9dcc6 35%,#d8e8c8 58%,#eef7e8 72%,#f2f9ee 100%)}
.locator-title{left:466px;top:22px;font-family:"Jost",sans-serif;font-weight:600;font-size:26px;color:var(--ink)}
.locator-input{left:398px;top:65px;width:345px;height:44px;background:#fff;border:1px solid #d4d4d4;
  font-family:"Jost",sans-serif;font-size:21px;color:#777;display:flex;align-items:center;justify-content:center}
.locator-button{left:470px;top:117px;width:203px;height:45px;background:var(--button-grey);color:#fff;
  font-family:"Jost",sans-serif;font-size:16px;display:flex;align-items:center;justify-content:center}

.contacts-title{right:154px;top:497px;font-family:"Jost",sans-serif;font-weight:600;font-size:24px;color:var(--ink)}
.contacts-detail{right:154px;top:563px;width:150px;text-align:right;font-family:"Open Sans",sans-serif;font-size:9.5px;line-height:13px;color:#666}
.contacts-detail .phones{margin-top:13px}
.contacts-detail .num{color:var(--link-blue)}
.dot{display:inline-block;width:8px;height:8px;border-radius:50%;background:var(--link-blue);vertical-align:-1px;margin:0 2px}

.footer{left:0;top:683px;width:1200px;height:163px;background:var(--footer)}
.social{left:511px;top:54px;display:flex;gap:4px}
.social span{width:32px;height:32px;display:block}
.footer-nav{left:0;top:101px;width:1200px;text-align:center;font-family:"Open Sans",sans-serif;font-size:13.6px;color:var(--footer-link);word-spacing:1px}
.footer-nav .sep{margin:0 6px}

.legal{left:0;top:846px;width:1200px;height:46px;background:var(--green);color:#fff;
  font-family:"Open Sans",sans-serif;font-size:10.8px;display:flex;align-items:center;justify-content:center}
.legal b{text-decoration:underline;margin:0 3px}

.base{left:0;top:887px;width:1200px;height:113px;background:var(--base)}
.sheet-label{right:28px;top:34px;font-family:"Jost",sans-serif;font-size:44px;color:#fff;letter-spacing:.5px}
.sheet-label b{font-weight:600}
</style>
</head>
<body>

<section class="abs intro">
  <h2 class="abs section-title about-title"><span class="accent">ABOUT</span> US</h2>
  <div class="abs about-copy">
    <p>Lorem Ipsum is simply dummy text of the printing and typesetting industry. Lorem Ipsum has been the industry's standard dummy text ever since the 1500s, when an unknown printer took a galley of type and scrambled it to make a type specimen book. It has survived not only five centuries, but also the leap into electronic typesetting, remaining essentially unchanged. It was popularised in the 1960s with the release of Lettrafix sheets containing Lorem Ipsum passages, and more recently with desktop publishing software like Pressline Layout including versions of Lorem Ipsum.</p>
    <p>Lorem Ipsum is simply dummy text of the printing and typesetting industry. Lorem Ipsum has been the industry's standard dummy text ever since the 1500s, when an unknown printer took a galley of type and scrambled it to make a type specimen book. It has survived not only five centuries, but also the leap into electronic typesetting, remaining essentially unchanged.</p>
  </div>

  <div class="abs signup" role="img" aria-label="Photo of a sunlit golf course lawn with trees and a pond with a wooden footbridge">
    <div class="abs signup-panel"></div>
    <h2 class="abs section-title signup-title"><span class="accent">GET</span> STARTED</h2>
    <div class="field" style="top:56px">First Name</div>
    <div class="field" style="top:95px">Last Name</div>
    <div class="field" style="top:135px">Email Address</div>
    <div class="field" style="top:172px">Phone Number</div>
    <div class="field message" style="top:210px">Type your message here</div>
    <div class="abs submit">SUBMIT</div>
  </div>
</section>

<div class="abs locator" role="img" aria-label="Illustrated aerial town map with streets, buildings and green park areas">
  <div class="abs locator-title">FIND A LOCATION</div>
  <div class="abs locator-input">City &amp; State or ZIP Code</div>
  <div class="abs locator-button">FIND NOW!</div>
</div>

<h2 class="abs contacts-title">CONTACTS</h2>
<div class="abs contacts-detail">
  <div>4120 - 4124 Larkspur Lane<br>Fernbrook, FB12 4KT</div>
  <div class="phones">Freephone: <span class="dot"></span><span class="num">+1 800 555<br>0142</span> Telephone: <span class="dot"></span><span class="num">+1 800 555<br>0187</span></div>
</div>

<footer class="abs footer">
  <div class="abs social" aria-label="Social links">
    <span style="background:#7a7c80"></span>
    <span style="background:#85878b"></span>
    <span style="background:#7a7c80"></span>
    <span style="background:#85878b"></span>
    <span style="background:#3a3a3c"></span>
  </div>
  <nav class="abs footer-nav">SERVICES<span class="sep">|</span>LOCATIONS<span class="sep">|</span>CONSULTANTS<span class="sep">|</span>FAQ<span class="sep">|</span>CONTACT</nav>
</footer>

<div class="abs legal">Copyright © 2014 Meadowfield Turf Crew. Use of this website constitutes acceptance of our <b>User Agreement</b> and <b>Privacy Policy</b></div>

<div class="abs base">
  <div class="abs sheet-label">Mockup <b>2 of 2</b></div>
</div>

</body>
</html>
```